DW&P Business Card Design

We need a business card designed for two firm who have merged. We are a Private Wealth Management firm with CPA's, Financial Advisors, Research Analysts, Attorneys who service high net worth clients. The final design should communicate class and not so much flash. Integrity, Trust, wealth. Think old school law firm or old school wall street. Attached is a pdf of our current temporary card.
Target Market(s)
People 45-70 who have considerable wealth
Industry/Entity Type
School
Contact Information for Business Card
Dunmore, WelTigan & Associates, Private Wealth Management, Glen WelTigan, Managing Partner, Senior Portfolio Manager, 2600 9th Avenue, Suite410, Sarasota, Florida 34871, Phone (941) 555-0147, Fax (941) 555-0193, glen@dunmorewelt-example.com
Look and feel
Each slider illustrates characteristics of the customer's brand and the style your logo design should communicate.

```html
<!DOCTYPE html>
<html lang="en">
<head>
<meta charset="utf-8">
<title>DW&amp;P Business Card</title>
<link rel="stylesheet" href="https://fonts.googleapis.com/css2?family=Oswald:wght@600&family=Tinos&family=Open+Sans:wght@700&display=swap">
<style>
  :root {
    --canvas: #ffffff;
    --card: #e4e4e4;
    --royal: #0a2cea;
    --ink: #111111;
    --paper: #ffffff;
    --sky: #4fd6ff;
  }
  * { margin: 0; padding: 0; box-sizing: border-box; }
  html, body { width: 965px; height: 1200px; overflow: hidden; background: var(--canvas); }
  .sheet { position: relative; width: 965px; height: 1200px; }
  .card { position: absolute; background: var(--card); }
  .card--front { left: 24px; top: 12px; width: 898px; height: 572px; }
  .card--back { left: 24px; top: 600px; width: 898px; height: 572px; }
  .panel { position: absolute; background: var(--royal); }
  .panel--side { left: 82px; top: 6px; width: 297px; height: 580px; }
  .panel--band { left: 20px; top: 740px; width: 910px; height: 282px; }
  .mark { position: absolute; display: flex; align-items: center; gap: 12px; }
  .mark__dot { width: 26px; height: 26px; border-radius: 50%; background: var(--sky); }
  .mark__name { font-family: "Open Sans", sans-serif; font-weight: 700; font-size: 58px; color: var(--paper); line-height: 1; }
  .mark--front { left: 112px; top: 232px; }
  .mark--back { left: 140px; top: 843px; }
  .abs { position: absolute; line-height: 1; white-space: nowrap; }
  .firm { font-family: "Oswald", sans-serif; font-weight: 600; font-size: 34px; transform: scaleX(0.92); transform-origin: center; }
  .tagline { font-family: "Tinos", serif; font-size: 28px; }
  .holder { font-family: "Open Sans", sans-serif; font-weight: 700; color: var(--paper); text-align: center; width: 297px; left: 82px; }
  .holder__name { top: 385px; font-size: 32px; }
  .holder__role { top: 424px; font-size: 23px; }
  .holder__title { top: 461px; font-size: 19px; }
  .front-firm { left: 415px; width: 476px; text-align: center; top: 154px; color: var(--ink); }
  .front-tag { left: 415px; width: 476px; text-align: center; top: 202px; color: var(--ink); }
  .contact { font-family: "Tinos", serif; font-size: 24px; color: var(--ink); text-align: right; right: 76px; }
  .contact--a1 { top: 316px; right: 76px; }
  .contact--a2 { top: 352px; right: 92px; }
  .contact--phone { top: 422px; right: 92px; }
  .contact--fax { top: 453px; right: 92px; }
  .contact--mail { top: 484px; right: 88px; }
  .back-firm { left: 400px; width: 476px; text-align: center; top: 834px; color: var(--paper); }
  .back-tag { left: 400px; width: 476px; text-align: center; top: 886px; color: var(--paper); }
</style>
</head>
<body>
<main class="sheet">
  <section class="card card--front" aria-label="Card front"></section>
  <div class="panel panel--side"></div>
  <div class="mark mark--front"><span class="mark__dot"></span><span class="mark__name">DW&amp;P</span></div>
  <p class="abs holder holder__name">Glen WelTigan</p>
  <p class="abs holder holder__role">Managing Partner</p>
  <p class="abs holder holder__title">Senior Portfolio Manager</p>
  <h1 class="abs firm front-firm">Dunmore, WelTigan &amp; Associates</h1>
  <p class="abs tagline front-tag">Private Wealth Management</p>
  <p class="abs contact contact--a1">2600 9th Avenue, Suite410,</p>
  <p class="abs contact contact--a2">Sarasota, Florida 34871</p>
  <p class="abs contact contact--phone">Phone : (941) 555-0147</p>
  <p class="abs contact contact--fax">Fax&nbsp; : (941) 555-0193</p>
  <p class="abs contact contact--mail">E-mail : glen@dunmorewelt-example.com</p>

  <section class="card card--back" aria-label="Card back"></section>
  <div class="panel panel--band"></div>
  <div class="mark mark--back"><span class="mark__dot"></span><span class="mark__name">DW&amp;P</span></div>
  <h2 class="abs firm back-firm">Dunmore, WelTigan &amp; Associates</h2>
  <p class="abs tagline back-tag">Private Wealth Management</p>
</main>
</body>
</html>
```